Banner Ad Design Project: rovalenmotors.com

Google all ad dimensions banner pack for http://www.rovalenmotors.com.

Ad dimensions Max. file sizes (KB) Ad types
468 × 60 50 Banner
728 × 90 50 Leaderboard
250 × 250 50 Square
200 × 200 50 Small square
336 × 280 50 Large rectangle
300 × 250 50 Inline rectangle
120 × 600 50 Skyscraper
160 × 600 50 Wide skyscraper
300 × 600 200 Half-page ad
970 × 90 200 Large leaderboard
240 × 400 50 Vertical rectangle
980 × 120 200 Panorama
930 × 180 200 Top banner
250 × 360 50 Triple widescreen
580 × 400 200 Netboard

*Please visit the website and come up with unique ideas.

Target Market(s)

Consumers looking to transport a car, motor vehicle, motorcycle or anything that has wheels and a motor in the united states long distance.

Industry/Entity Type

Google

Requirements
Must have
• a call to action for example (RANDOM ONE):
-
TALK TO A REAL CAR SHIPPING PRO NOW: 1-888-514-2763
HAVE CAR TRANSPORT QUESTIONS? CALL NOW: 1-888-514-2763
CALL NOW & TALK TO A REAL AUTO SHIPPING EXPERT: 1-888-514-2763
Call Now Free Quote:1-888-514-2763

Nice to have
• Best Value For Dollar Auto Transport
Bonded, Insured & Licensed
Price Match Guarantee: will match any price by a 4 or 5 star rated Company.
Best of all, you pay nothing until your car is picked up!
Nationwide Door-To-Door Vehicle Shipping
Should not have
• Logo integrated in to the design.
bold call to action; ex; call now free quote:
Heading style phone number, 888-514-2763, stands out and screams call now.
example:
CALL ROVALEN TODAY TO TRANSPORT YOUR VEHICLE
1-888-514-2763

```html
<!DOCTYPE html>
<html lang="en">
<head>
<meta charset="utf-8">
<title>Rovalen Motors – Banner</title>
<link href="https://fonts.googleapis.com/css2?family=Roboto+Condensed:wght@400;700&display=swap" rel="stylesheet">
<style>
  :root {
    --canvas: #ffffff;
    --frame: #2b2b2b;
    --blue-deep: #3a7fc2;
    --blue-mid: #6ea6d8;
    --blue-pale: #d6e7f5;
    --white: #ffffff;
    --ink: #1f1f1f;
    --headline-edge: #1c2f45;
    --brand: #3d77a8;
    --car-white: #e6e9ec;
    --car-red: #c8202a;
    --car-silver: #cfd3d6;
  }
  html, body {
    margin: 0;
    padding: 0;
    width: 1200px;
    height: 1000px;
    overflow: hidden;
    background: var(--canvas);
  }
  .banner {
    position: absolute;
    left: 299px;
    top: 419px;
    width: 598px;
    height: 158px;
    border: 2px solid var(--frame);
    overflow: hidden;
    background: linear-gradient(100deg, var(--blue-deep) 0%, var(--blue-mid) 35%, var(--blue-pale) 60%, var(--white) 72%, var(--white) 100%);
  }
  .headline {
    position: absolute;
    margin: 0;
    font-family: "Roboto Condensed", "Arial Narrow", sans-serif;
    font-weight: 700;
    color: var(--white);
    text-shadow:
      1px 1px 0 var(--headline-edge), -1px -1px 0 var(--headline-edge),
      1px -1px 0 var(--headline-edge), -1px 1px 0 var(--headline-edge),
      2px 2px 2px rgba(0,0,0,0.5);
    white-space: nowrap;
    line-height: 1;
    transform-origin: left top;
  }
  .headline--lead { left: 12px; top: 11px; font-size: 24px; transform: scaleX(0.87); }
  .headline--phone { left: 57px; top: 38px; font-size: 32px; transform: scaleX(0.75); }
  .perks {
    position: absolute;
    left: 12px;
    top: 79px;
    margin: 0;
    padding: 0;
    list-style: none;
    font-family: "Roboto Condensed", "Arial Narrow", sans-serif;
    font-weight: 400;
    font-size: 13.2px;
    color: var(--ink);
    line-height: 19px;
    white-space: nowrap;
  }
  .vehicle-photos {
    position: absolute;
    left: 333px;
    top: 10px;
    width: 265px;
    height: 56px;
    display: flex;
    gap: 8px;
  }
  .vehicle-photos span {
    flex: 1;
    border-radius: 22px 22px 10px 10px;
  }
  .vehicle-photos .car-white { background: linear-gradient(180deg, #f4f5f6, var(--car-white)); }
  .vehicle-photos .car-red { background: linear-gradient(180deg, #de3a40, var(--car-red)); flex: 0.75; }
  .vehicle-photos .car-silver { background: linear-gradient(180deg, #eceef0, var(--car-silver)); }
  .brand {
    position: absolute;
    left: 428px;
    top: 102px;
    display: flex;
    align-items: center;
    gap: 10px;
    font-family: "Roboto Condensed", "Arial Narrow", sans-serif;
    font-weight: 700;
    font-size: 22px;
    color: var(--brand);
    letter-spacing: 0.5px;
  }
  .brand__mark {
    width: 34px;
    height: 34px;
    border-radius: 50%;
    background: var(--brand);
  }
</style>
</head>
<body>
  <section class="banner" aria-label="Rovalen Motors car shipping banner">
    <h1 class="headline headline--lead">TALK TO A REAL CAR SHIPPING PRO</h1>
    <p class="headline headline--phone">NOW: 1-888-514-2763</p>
    <ul class="perks">
      <li>• Best Value For Dollar Auto Transport • Bonded, Insured &amp; Licensed</li>
      <li>• Price Match Guarantee: will match any price by a 4 or&nbsp; 5 star rated Company.</li>
      <li>• Best of all, you pay nothing until your car is picked up!</li>
      <li>• Nationwide Door-To-Door Vehicle Shipping</li>
    </ul>
    <div class="vehicle-photos" role="img" aria-label="Photos of three sedans: white, red and silver">
      <span class="car-white"></span>
      <span class="car-red"></span>
      <span class="car-silver"></span>
    </div>
    <div class="brand">
      <span class="brand__mark" aria-hidden="true"></span>
      <span class="brand__name">ROVALEN</span>
    </div>
  </section>
</body>
</html>
```